Help me create an amazing cover for my first ebook!!

I am looking to have a modern and professional looking cover for my first ebook. It will be published through Borvex Quill Self Press and will need to follow their formatting and guidelines. I want the cover to have a modern and vibrant feel, that appeals to a millennial audience. This is a real estate book that is focused on a niche category catered to young professionals, so the idea would be to appeal to them.

Title:
The Twentysomething Playbook for Duplex Living

A Smart Property Buying Plan to Start Early, Cut Your Housing Costs (Sometimes to Zero), and Speed Up Your Path to Lasting Wealth.

Davin Osterlund

Target Market(s)

Real Estate investors, investors, millennials, young professionals, college educated, 20-40 years old.Financial freedom, finance.

Industry/Entity Type

Real Estate

Font styles to use
Sans Serif

Colors

Designer to choose colors to be used in the design.

Requirements
Must have
• Must follow the borvex quill self press format. I attached a screenshot of the details, it can also be found here: https://qsp.borvexbooks.example/en_US/help/topic/R481736025
• Must include this title:
• The Twentysomething Playbook for Duplex Living
• A Smart Property Buying Plan to Start Early, Cut Your Housing Costs (Sometimes to Zero), and Speed Up Your Path to Lasting Wealth.
• Davin Osterlund.
• I added examples of book covers I like to use as a guide, I also added some color pallette examples.
Nice to have
• Modern, clean design that's not too busy. Some sort of simple photo or illustration to incorporate in the cover along with the text would be nice.

```html
<!DOCTYPE html>
<html lang="en">
<head>
<meta charset="utf-8">
<title>The Twentysomething Playbook for Duplex Living — Cover</title>
<link rel="stylesheet" href="https://fonts.googleapis.com/css2?family=Raleway:wght@200;300&family=Tinos:ital,wght@0,400;0,700;1,700&display=swap">
<style>
  :root {
    --backdrop: #d4e9f5;
    --cover-red-core: #d10b0b;
    --cover-red-mid: #b80606;
    --cover-red-edge: #950404;
    --title-white: #ffffff;
    --accent-orange: #f7a300;
    --art-placeholder-top: rgba(255, 255, 255, 0.16);
    --art-placeholder-bottom: rgba(255, 255, 255, 0.06);
  }
  * { margin: 0; padding: 0; box-sizing: border-box; }
  html, body {
    width: 1200px;
    height: 1200px;
    overflow: hidden;
    background: var(--backdrop);
  }
  .canvas {
    position: relative;
    width: 1200px;
    height: 1200px;
  }
  .cover {
    position: absolute;
    left: 298px;
    top: 95px;
    width: 606px;
    height: 970px;
    background: radial-gradient(ellipse 70% 60% at 50% 52%, var(--cover-red-core) 0%, var(--cover-red-mid) 55%, var(--cover-red-edge) 100%);
    color: var(--title-white);
    text-align: center;
  }
  .book-title {
    font-weight: 400;
  }
  .book-title > span {
    position: absolute;
    left: 0;
    width: 100%;
    padding-right: 34px;
    line-height: 1;
    white-space: nowrap;
  }
  .title-lead {
    top: 72px;
    padding-left: 46px;
    font-family: "Tinos", "Times New Roman", serif;
    font-weight: 400;
    font-size: 32px;
  }
  .title-light {
    top: 104px;
    font-family: "Raleway", "Helvetica Neue", sans-serif;
    font-weight: 200;
    font-size: 50px;
    letter-spacing: -0.5px;
  }
  .title-main {
    top: 172px;
    font-family: "Tinos", "Times New Roman", serif;
    font-weight: 700;
    font-size: 108px;
    letter-spacing: -3px;
  }
  .title-tail {
    top: 334px;
    font-family: "Tinos", "Times New Roman", serif;
    font-weight: 400;
    font-size: 46px;
    color: var(--accent-orange);
  }
  .title-tail strong { font-weight: 700; }
  .cover-art {
    position: absolute;
    left: 167px;
    top: 415px;
    width: 320px;
    height: 280px;
    border-radius: 12px;
    background: linear-gradient(180deg, var(--art-placeholder-top) 0%, var(--art-placeholder-bottom) 100%);
  }
  .subtitle {
    position: absolute;
    top: 742px;
    left: 0;
    width: 100%;
    font-family: "Tinos", "Times New Roman", serif;
    font-size: 17px;
    line-height: 20px;
  }
  .subtitle em {
    display: block;
    font-weight: 700;
    font-style: italic;
  }
  .author {
    position: absolute;
    top: 880px;
    left: 0;
    width: 100%;
    padding-left: 20px;
    font-family: "Tinos", "Times New Roman", serif;
    font-weight: 700;
    font-size: 46px;
    line-height: 1;
    color: var(--accent-orange);
  }
</style>
</head>
<body>
<main class="canvas">
  <section class="cover" aria-label="Book cover">
    <h1 class="book-title">
      <span class="title-lead">The</span>
      <span class="title-light">Twentysomething</span>
      <span class="title-main">Playbook</span>
      <span class="title-tail">for <strong>Duplex Living</strong></span>
    </h1>
    <div class="cover-art" role="img" aria-label="Illustration area: a house-shaped key turning in a door lock"></div>
    <p class="subtitle">
      <em>A Smart Property Buying Plan</em>
      to Start Early, Cut Your Housing Costs (Sometimes to Zero),<br>
      and Speed Up Your Path to Lasting Wealth.
    </p>
    <p class="author">Davin Osterlund</p>
  </section>
</main>
</body>
</html>
```